Ashcombe Rise Brochure - A new residential property investment development in Brisbane Queensland *

I need a brochure to entice and inspire customers of financial planners and alike to buy our investment property development, Ashcombe Rise in Greenbank, Australia.

The brochure will be approximately 16 - 18 pages long and will follow a similar format (including maps etc) to the once attached in the uploaded files, however it is important that it has it's own unique style and brand identify. You will have access to all the renders, maps and autocad drawings that will need to be included in the brochure and will be linked in my dropbox link below.

The brochure should feel sophisticated and use the logo we've previously had developed on pixel forge. The background and text should also match the style guidelines of our logo's although happy for you to to get creative with the background as long as it is relevant and fits with the colours. For example stock photo's of tree's, people playing, sunlight etc are great - although the context should be in Australia.

There will be a bit of back and forth once I select the winning designer to ensure the brochure is perfect. I'll also need individual files of the masterplan.

Look forward to seeing your designs.

https://www.shelfbin.net/sh/qpxmtr4kd8wzv2n/BBTm7hsK9_PPQeYc4Jn2rdx8vo?dl=0

Target Market(s)

Financial Planners and their consumer customers

Industry/Entity Type

Real Estate Development

Other font styles liked:
• Monserrat - as per branding guidelines

Requirements
Must have
• At least all the elements that exist in the example brochures and outlined in the content

dropbox link - https://www.shelfbin.net/sh/qpxmtr4kd8wzv2n/BBTm7hsK9_PPQeYc4Jn2rdx8vo?dl=0

```html
<!DOCTYPE html>
<html lang="en">
<head>
<meta charset="utf-8">
<title>Ashcombe Rise Brochure</title>
<link href="https://fonts.googleapis.com/css2?family=Cormorant+Garamond:wght@500&family=Montserrat:wght@400;500;600;700&family=Open+Sans:wght@400&display=swap" rel="stylesheet">
<style>
:root{
  --navy:#1d5680;
  --navy-deep:#164769;
  --navy-ink:#1a4f78;
  --paper:#ffffff;
  --backdrop:#e3e4e6;
  --rule:#c9ced4;
  --ink:#2a2f36;
  --serif:"Cormorant Garamond", Georgia, serif;
  --sans:"Montserrat", Arial, sans-serif;
}
*{margin:0;padding:0;box-sizing:border-box}
html,body{width:1200px;height:2935px;overflow:hidden}
body{background:linear-gradient(180deg,#e9eaec 0%,var(--backdrop) 100%);font-family:var(--sans);color:var(--ink);position:relative}
.abs{position:absolute}
.wordmark{font-family:var(--serif);font-weight:500;letter-spacing:1px;text-transform:uppercase;white-space:nowrap}
.page{position:absolute;background:var(--paper);box-shadow:0 2px 8px rgba(0,0,0,.18);overflow:hidden}
.blue{background:linear-gradient(180deg,var(--navy) 0%,var(--navy-deep) 100%)}
.art{position:absolute}
.pgnum{position:absolute;width:20px;height:20px;border-radius:50%;background:var(--navy);color:#fff;font-size:9px;font-weight:600;display:flex;align-items:center;justify-content:center}
.foot-mark{position:absolute;left:15px;font-size:14px;color:var(--navy)}

/* presentation header */
.hero-mark{left:74px;top:122px;font-size:46px;color:var(--navy)}
.hero-cover{left:300px;top:215px;width:780px;height:550px}
.hero-cover .wordmark{position:absolute;left:0;right:0;top:80px;text-align:center;color:#fff;font-size:48px}
.hero-cover .art{left:70px;top:190px;width:640px;height:280px;background:linear-gradient(100deg,rgba(255,255,255,.10),rgba(255,255,255,.22),rgba(255,255,255,.10));border-radius:150px 24px 150px 24px}
.sheet-title{left:0;right:0;top:888px;text-align:center;font-family:"Open Sans",Arial,sans-serif;font-size:37px;color:#1b1b1b;letter-spacing:.5px}
.sheet-title span{border-bottom:2px solid #1b1b1b;padding-bottom:1px}

/* cover page */
.cover .wordmark{position:absolute;left:0;right:0;top:74px;text-align:center;color:#fff;font-size:30px}
.cover .art{left:0;top:128px;width:500px;height:210px;background:linear-gradient(100deg,rgba(255,255,255,.08),rgba(255,255,255,.24),rgba(255,255,255,.08));border-radius:140px 10px 140px 10px}

/* contents */
.toc-side{position:absolute;left:0;top:0;width:250px;height:100%}
.toc-side h2{position:absolute;left:0;right:0;top:48px;text-align:center;font-family:var(--serif);font-weight:500;color:#fff;font-size:27px;line-height:28px;letter-spacing:.5px}
.toc-side .art{left:0;top:118px;width:250px;height:130px;background:linear-gradient(100deg,rgba(255,255,255,.08),rgba(255,255,255,.24),rgba(255,255,255,.08));border-radius:90px 10px 90px 10px}
.toc-side .wordmark{position:absolute;left:0;right:0;top:288px;text-align:center;color:#fff;font-size:19px}
.toc-list{position:absolute;left:275px;top:74px;width:200px;list-style:none}
.toc-list li{font-size:10px;text-align:center;height:27px;line-height:26px;border-bottom:1px solid var(--rule);color:#222}
.toc-list li:last-child{border-bottom:none}
.toc-right{position:absolute;left:250px;top:0;right:0;bottom:0;background:linear-gradient(180deg,#fafafb,#eceef0)}

/* intro */
.intro-box{position:absolute;left:78px;top:107px;width:343px;height:163px;border:1px solid var(--navy)}
.intro-box h3{position:absolute;left:50%;top:-11px;transform:translateX(-50%);background:#fff;padding:0 8px;font-family:var(--serif);font-weight:500;color:var(--navy);font-size:20px;letter-spacing:1px;white-space:nowrap;line-height:20px}
.intro-box .copy{position:absolute;left:22px;right:22px;top:24px;text-align:center;font-size:5.6px;line-height:7px;color:#333}
.intro-box .copy p{margin-bottom:5px}

/* spread */
.spread-page{top:1738px;height:361px;width:511px}
.spread-footer{position:absolute;left:0;right:0;bottom:0;height:54px;background:#fff}

/* closing */
.closing{left:86px;top:2140px;width:1024px;height:724px}
.closing-band{position:absolute;left:0;top:0;width:100%;height:361px}
.closing-band .divider{position:absolute;left:512px;top:0;width:1px;height:100%;background:rgba(255,255,255,.35)}
.closing-band .big-mark{position:absolute;left:0;width:512px;top:190px;text-align:center;color:#fff;font-size:46px}
.contact{position:absolute;left:611px;top:40px;color:#fff}
.contact h4{font-size:20px;font-weight:700;line-height:26px;margin-bottom:20px}
.contact .item{display:flex;gap:10px;margin-bottom:18px}
.contact .item svg{flex:none;margin-top:1px}
.contact .label{font-size:16px;font-weight:700;line-height:20px}
.contact .value{font-size:15px;font-weight:500;line-height:20px}
.brands{position:absolute;left:0;top:361px;width:100%;height:363px;background:#fff}
.brands h5{position:absolute;left:0;right:0;top:36px;text-align:center;font-size:20px;font-weight:700;color:var(--navy-ink)}
.brand-row{position:absolute;left:0;right:0;display:flex;justify-content:center;gap:38px}
.brand{display:flex;align-items:center;gap:5px;font-size:13px;font-weight:600;color:#2a2f36;white-space:nowrap}
.brand i{display:inline-block;width:10px;height:10px;background:var(--navy)}
</style>
</head>
<body>

<!-- presentation header -->
<div class="abs wordmark hero-mark">Ashcombe Rise</div>
<div class="page blue hero-cover">
  <div class="wordmark">Ashcombe Rise</div>
  <div class="art" role="img" aria-label="Large white willow branch illustration across the cover"></div>
</div>
<div class="abs sheet-title"><span>ASHCOMBE RISE BROCHURE</span></div>

<!-- cover -->
<div class="page blue cover" style="left:86px;top:966px;width:500px;height:354px">
  <div class="wordmark">Ashcombe Rise</div>
  <div class="art" role="img" aria-label="White willow branch illustration sweeping across the cover"></div>
</div>

<!-- contents -->
<div class="page" style="left:610px;top:966px;width:499px;height:354px">
  <div class="toc-right"></div>
  <div class="toc-side blue">
    <h2>TABLE OF<br>CONTENTS</h2>
    <div class="art" role="img" aria-label="White willow branch illustration"></div>
    <div class="wordmark">Ashcombe Rise</div>
  </div>
  <ul class="toc-list">
    <li>About</li>
    <li>Location proximity</li>
    <li>Sense of community</li>
    <li>Investment</li>
    <li>Points of interest</li>
    <li>Masterplan</li>
    <li>House plans</li>
    <li>Package Inclusions</li>
  </ul>
  <div class="pgnum" style="left:468px;top:323px">01</div>
</div>

<!-- photo page -->
<div class="page" style="left:86px;top:1347px;width:500px;height:353px">
  <div class="art" role="img" aria-label="Photo of a tall tree in a misty golden meadow at sunrise with mountains behind" style="left:0;top:0;width:328px;height:310px;background:linear-gradient(180deg,#8fb3c6 0%,#d9b77a 38%,#a59a63 58%,#5f7a2c 80%,#3f5e1e 100%)"></div>
  <div class="art" role="img" aria-label="Photo of a beach shoreline with birds over the water at sunset" style="left:334px;top:0;width:166px;height:114px;background:linear-gradient(180deg,#5f9cc6 0%,#a9cfe4 45%,#e7d9b8 70%,#bfa47e 100%)"></div>
  <div class="art" role="img" aria-label="Photo of two children fishing from a log over a calm green creek" style="left:334px;top:120px;width:166px;height:190px;background:linear-gradient(180deg,#cfe3b0 0%,#8fb470 45%,#6e8f5a 70%,#9ab19a 100%)"></div>
  <div class="wordmark foot-mark" style="top:330px">Ashcombe Rise</div>
  <div class="pgnum" style="left:468px;top:322px">02</div>
</div>

<!-- introduction -->
<div class="page" style="left:610px;top:1347px;width:499px;height:353px;background:linear-gradient(180deg,#fff,#eef0f2)">
  <div class="intro-box">
    <h3>INTRODUCTION</h3>
    <div class="copy">
      <p>Pull out – an opportunity to invest in long term value creation</p>
      <p>Welcome to Ashcombe Rise, an exclusively crafted neighbourhood creating better communities to bring people together.</p>
      <p>Ashcombe Rise has been designed to create an inviting sense of place, with access to superior home design and generous inclusions as standard. Our approach ensures contemporary, comfortable living.</p>
      <p>Nestled between Brisbane and the Gold Coast, Ashcombe Rise is located close to key amenities, services, public transport and major road networks.</p>
      <p>With a limited number of homes available, an investment in Ashcombe Rise provides a unique wealth creation opportunity for the astute investor.</p>
    </div>
  </div>
  <div class="wordmark foot-mark" style="top:330px">Ashcombe Rise</div>
  <div class="pgnum" style="left:468px;top:322px">03</div>
</div>

<!-- masterplan spread -->
<div class="page spread-page" style="left:86px">
  <div class="spread-footer"></div>
  <div class="wordmark foot-mark" style="top:335px">Ashcombe Rise</div>
  <div class="pgnum" style="left:480px;top:327px">04</div>
</div>
<div class="page spread-page" style="left:598px">
  <div class="spread-footer"></div>
  <div class="wordmark foot-mark" style="top:335px">Ashcombe Rise</div>
  <div class="pgnum" style="left:477px;top:327px">05</div>
</div>
<div class="art" role="img" aria-label="Aerial render of the estate showing two rows of new homes along a curving street with surrounding trees" style="left:86px;top:1738px;width:1023px;height:307px;background:linear-gradient(180deg,#4d6440 0%,#9ea8a4 22%,#c9ced0 34%,#6d7773 48%,#5d6864 55%,#c4c9cb 66%,#9aa39f 78%,#415a36 100%)"></div>
<div class="abs" style="left:598px;top:1738px;width:1px;height:361px;background:rgba(0,0,0,.12)"></div>

<!-- closing -->
<div class="page closing">
  <div class="closing-band blue">
    <div class="divider"></div>
    <div class="wordmark big-mark">Ashcombe Rise</div>
    <div class="contact">
      <h4>To find out how to secure your<br>investment in Ashcombe Rise,<br>contact us now.</h4>
      <div class="item">
        <svg width="20" height="20" viewBox="0 0 20 20"><circle cx="10" cy="10" r="10" fill="#fff"/><path d="M7 5.5l1.6 2.2-1 1.2c.7 1.4 1.8 2.5 3.2 3.2l1.2-1 2.2 1.6-.8 1.8c-4-.3-7.4-3.7-7.7-7.7z" fill="#1d5680"/></svg>
        <div><div class="label">Call</div><div class="value">1300 555 018</div></div>
      </div>
      <div class="item">
        <svg width="20" height="20" viewBox="0 0 20 20"><circle cx="10" cy="10" r="10" fill="#fff"/><rect x="5" y="6.5" width="10" height="7" rx="1" fill="none" stroke="#1d5680" stroke-width="1.4"/><path d="M5.5 7l4.5 3.5L14.5 7" fill="none" stroke="#1d5680" stroke-width="1.4"/></svg>
        <div><div class="label">Email</div><div class="value">sales@ashcomberise.com.au</div></div>
      </div>
      <div class="item">
        <svg width="20" height="20" viewBox="0 0 20 20"><circle cx="10" cy="10" r="10" fill="#fff"/><path d="M10 4.5a3.6 3.6 0 0 0-3.6 3.6c0 2.7 3.6 6.9 3.6 6.9s3.6-4.2 3.6-6.9A3.6 3.6 0 0 0 10 4.5z" fill="#1d5680"/><circle cx="10" cy="8.1" r="1.3" fill="#fff"/></svg>
        <div><div class="label">Address</div><div class="value">100 Marlow Rd, Kestrel Vale QLD 4300</div></div>
      </div>
    </div>
  </div>
  <div class="brands">
    <h5>Working with some of Australia’s leading brands</h5>
    <div class="brand-row" style="top:100px"><span class="brand"><i></i>Corlan</span><span class="brand">Venna</span><span class="brand"><i></i>Harbor Doors</span><span class="brand">Ridgeway Tiles</span><span class="brand"><i></i>Tallis</span></div>
    <div class="brand-row" style="top:164px"><span class="brand"><i></i>Brenn</span><span class="brand">Surfacia</span><span class="brand"><i></i>Calder Works</span><span class="brand">Oakfield Floors</span><span class="brand"><i></i>Voltline</span></div>
    <div class="brand-row" style="top:229px"><span class="brand"><i></i>Meridian Fixtures</span><span class="brand">Kavari</span><span class="brand"><i></i>Claystone Bricks</span><span class="brand">Shadewell Blinds</span><span class="brand"><i></i>Paintcraft</span></div>
    <div class="brand-row" style="top:293px"><span class="brand"><i></i>Rooftone</span><span class="brand">Lunara Baths</span><span class="brand"><i></i>Timberline Doors</span><span class="brand">Cladmark</span></div>
  </div>
</div>

</body>
</html>
```